USA Home and Kitchen "Multi-Product" Brand Needs a Stunning Packaging Design.

We need a new packaging design for our Brand: T&M Hearth & Nest. We Manufacture, Market, and Sell Home & Kitchen Products (Such as Kitchen Utensils and Home Decor to name a few) Direct to Consumers in the United States via our Website and Vendora.com. We would like to see designs that are simple, clean, and modern, yet stand out and demand attention. Our Preferred colors of the design should include: Black or Grey as the base color/shade), White or Grey for the text, and some additional color can be used for complementary elements/visuals at your own discretion or creativity. We would like this to be an Interchangeable Design that can be easily modified and implemented across all of our other products (i.e: does not contain too many images or design elements that reference a particular product.

Although this design and the concept as a whole is intended to be used across our entire catalogue of products. Please feel free to base your design on our one of our top selling products as per the following URL: https://www.vendora-shop.example/dp/X93QL4471Z?ref=abc_item_dp.

Target Market(s)

Our customers tend come from many areas across the spectrum. But the quintessential T&M target customer (the type of person who tends to be our most receptive and loyal customer) is female and part of the Millennials generation, aged in her 30s, and is either working full-time in a white-collar job or on home duties, of which she would have young children, a spouse, or other family members to look after. She’s part of the conventional family life who represent the core of ‘middle America’. She doesn’t mind to splurge every now and again on shopping for items that she wants and/or needs, whilst some of the time she’ll also go out of her way to ‘search for a bargain’. She tends to spend more time in her home and kitchen than the average individual. We recognize that cooking for herself and family, and providing a well furnished and stylish home is part of who she is.

Industry/Entity Type

Retail

Font styles to use
Serif
Sans Serif

Colors

Designer to choose only greyscale colors for use in the design.

Requirements
Must have
• Interchangeable Design (A "Universal" Packaging Design that can be easily modified and adapted for use with a large catalogue of products under our brand).
Nice to have
• Some visual elements that gives our packaging/brand the ability to stand out and be unique/memorable.
Should not have
• Our design should not have too much text. Nor should it be cluttered or overcrowded with too much information or visual elements. And does not contain too many images or design elements that reference a particular product. We believe simplicity is key, and quality over quantity.

```html
<!DOCTYPE html>
<html lang="en">
<head>
<meta charset="utf-8">
<title>T&amp;M Hearth &amp; Nest – Solid Turner Packaging</title>
<link href="https://fonts.googleapis.com/css2?family=Cormorant+Garamond:wght@500&family=Open+Sans:wght@600&display=swap" rel="stylesheet">
<style>
  :root {
    --backdrop: #222222;
    --box-face: #1b1b1b;
    --ornament-light: #9a9a9a;
    --ornament-dark: #3a3a3a;
    --silver: #c9c9c9;
    --label: #e6e6e6;
  }
  html, body {
    margin: 0;
    padding: 0;
    width: 1200px;
    height: 900px;
    overflow: hidden;
    background: var(--backdrop);
  }
  .canvas {
    position: relative;
    width: 1200px;
    height: 900px;
  }
  .box-front {
    position: absolute;
    left: 494px;
    top: 135px;
    width: 213px;
    height: 628px;
    background: var(--box-face);
    overflow: hidden;
  }
  .ornament {
    position: absolute;
    border-radius: 50%;
    opacity: 0.5;
    background: radial-gradient(circle, var(--ornament-light) 0%, var(--ornament-dark) 62%, transparent 72%);
  }
  .ornament--top {
    width: 340px;
    height: 340px;
    left: -100px;
    top: -170px;
  }
  .ornament--bottom {
    width: 290px;
    height: 290px;
    left: 70px;
    top: 485px;
  }
  .brand-name {
    position: absolute;
    left: 0;
    right: 0;
    top: 222px;
    margin: 0;
    text-align: center;
    font-family: "Cormorant Garamond", serif;
    font-weight: 500;
    color: var(--silver);
  }
  .brand-name__initials {
    display: block;
    font-size: 92px;
    line-height: 1;
    letter-spacing: -1px;
  }
  .brand-name__words {
    display: block;
    margin-top: 26px;
    font-size: 15px;
    line-height: 1;
    letter-spacing: 3px;
    text-transform: uppercase;
  }
  .product-name {
    position: absolute;
    left: 0;
    right: 0;
    top: 462px;
    margin: 0;
    text-align: center;
    font-family: "Open Sans", sans-serif;
    font-weight: 600;
    font-size: 13.5px;
    letter-spacing: 0.3px;
    color: var(--label);
  }
</style>
</head>
<body>
  <main class="canvas">
    <section class="box-front">
      <div class="ornament ornament--top" role="img" aria-label="Fine silver line mandala ornament, top corner"></div>
      <div class="ornament ornament--bottom" role="img" aria-label="Fine silver line mandala ornament, bottom corner"></div>
      <h1 class="brand-name">
        <span class="brand-name__initials">T&amp;M</span>
        <span class="brand-name__words">Hearth &amp; Nest</span>
      </h1>
      <p class="product-name">SOLID TURNER</p>
    </section>
  </main>
</body>
</html>
```